Design a cover that embodies the concept of healing by Walking Out of the Fog

Subtitle: How to use tapping, applied kinesiology, and Chinese medicine to heal your body, free your mind and live in peace.

Tapping (Emotional Freedom Technique) is a modern mix of psychology and Chinese medicine that helps people to release the emotions they have inside that are contributing to the depression and anxiety they feel. Applied kinesiology or muscle testing is a biofeedback tool which helps to extract information from the body that can help people to profoundly heal. It can be used to determine whether heavy metals, heavy chemicals, food sensitivities or pathogens are causing the body problems. It can also be used to determine which supplements can help someone heal. This tool also can be used to identify emotions and memories that are also causing someone problems. Lastly, Chinese medicine uses food therapy, herbal formulas, meditation, tai chi (meditative movement), cupping and other tools to help people to be free of depression. This book is written to be information but also details my own personal journey of how I was able to heal from 11 years of heavy depression through the use of these tools.

The heart of the book is about emotional release, emotional freedom and emotional healing. You can surrender, release or let go of emotions and feel better very quickly. This certainly was my experience.

I would like the front and back cover to each be 8.5" x 5.5". I still have to get an ISBN number for the back page as well. Here is the text that I would like on the back cover for now: Millions of people feel the pain, loneliness, and agony of anxiety and depression every day. Many turn to Western medicine in the hopes that a pill will ease the pain and make the problem go away. Oftentimes, this only makes matters worse and doesn’t address the root cause. No one should have to struggle like this when natural answers exist that can address the physical, energetic, emotional, or spiritual causes of anxiety and depression. For 11 long years, Dr. Vance personally struggled with heavy depression until he discovered answers that helped him to completely heal. Walking Out of the Fog is a guide that will help you discover - The two root physical causes of depression and exactly what to do to start healing today - How the negative emotions we have stored within from trauma and bad experiences can drive depression - Tools from Chinese medicine, applied kinesiology, and tapping to help you free your mind and live in peace - An actionable plan to help you let go of the pain, suffering, and negative emotions from your past Whether you feel depressed and anxious or know someone who struggles with these issues, Walking Out of the Fog will transform how you think about depression and will give you the tools to heal so that you can be free and live in peace. Dr. Vance Holbrook is a board-certified acupuncture physician licensed in the state of Florida. He received his training at the Calder Institute of Holistic Practice. He also graduated with a master’s degree in counseling and psychology from Meadowbrook Seminary of Theology. His mission is to help people transform their health and improve the quality of their life naturally. He lives in Orlando, FL where he runs a holistic medical clinic called Bluepine Wellness Center. www.drvanceholbrook-example.com Instagram: drvanceholbrook Facebook: bluepinewellnesscenter

Target Market(s)

Those who suffer from depression and anxiety and want to heal naturally

Industry/Entity Type

Health And Wellness

Requirements
Must have
• My picture should be small and go on the back cover next to the information about me. The front cover would be all graphical. Thank you. On the front cover my name should be posted as "Dr. Vance Holbrook, AP, MA"

```html
<!DOCTYPE html>
<html lang="en">
<head>
<meta charset="utf-8">
<title>Walking Out of the Fog – Book Cover</title>
<link href="https://fonts.googleapis.com/css2?family=Bebas+Neue&family=Anton&family=Pathway+Gothic+One&family=Oswald:wght@300;600&display=swap" rel="stylesheet">
<style>
  :root {
    --teal: #68c6c4;
    --teal-soft: #a9dcda;
    --mist: #e4f3f2;
    --white: #ffffff;
    --ink: #000000;
    --charcoal: #3d3d3d;
    --photo-warm: #d9b393;
    --photo-light: #f4ecd2;
  }
  * { margin: 0; padding: 0; box-sizing: border-box; }
  html, body { width: 1200px; height: 897px; overflow: hidden; background: var(--white); }
  .cover { position: relative; width: 1200px; height: 897px; overflow: hidden; }

  /* Back cover + spine */
  .back-panel {
    position: absolute; left: 0; top: 0; width: 622px; height: 897px;
    background: var(--teal); color: var(--white);
  }
  .back-title {
    position: absolute; left: 0; top: 64px; width: 590px; text-align: center;
    font-family: "Bebas Neue", sans-serif; font-weight: 400; font-size: 56px; line-height: 1;
  }
  .back-blurb, .author-bio {
    position: absolute; width: 478px;
    font-family: "Pathway Gothic One", sans-serif; font-size: 17.2px; line-height: 22.8px;
  }
  .back-blurb { left: 53px; top: 131px; }
  .author-bio { left: 55px; top: 501px; }
  .author-bio strong { font-family: "Oswald", sans-serif; font-weight: 600; font-size: 14.5px; }
  .contact-list {
    position: absolute; left: 56px; top: 647px; list-style: none;
    font-family: "Oswald", sans-serif; font-weight: 600; font-size: 12.5px; line-height: 20px;
    color: var(--charcoal);
  }
  .author-photo {
    position: absolute; left: 420px; top: 646px; width: 112px; height: 136px;
    background: radial-gradient(ellipse 45% 40% at 50% 40%, var(--photo-light) 0%, var(--photo-warm) 100%);
    border: 3px solid var(--white);
  }
  .brand-name {
    position: absolute; left: 56px; top: 752px; display: flex; align-items: center; gap: 14px;
    font-family: "Oswald", sans-serif; font-weight: 600; font-size: 36px; line-height: 40px;
    color: var(--charcoal); text-transform: uppercase;
  }
  .brand-name .brand-square { width: 34px; height: 34px; background: var(--charcoal); }

  .spine-title, .spine-author {
    position: absolute; left: 584px; writing-mode: vertical-rl;
    color: var(--white); line-height: 1;
  }
  .spine-title { top: 212px; font-family: "Bebas Neue", sans-serif; font-size: 32px; }
  .spine-author { top: 542px; font-family: "Oswald", sans-serif; font-weight: 600; font-size: 26px; }

  /* Front cover */
  .front-author {
    position: absolute; left: 622px; top: 38px; width: 578px; text-align: center;
    font-family: "Anton", sans-serif; font-weight: 400; font-size: 48px; line-height: 1; color: var(--ink);
    white-space: nowrap;
  }
  .front-title {
    position: absolute; left: 622px; top: 104px; width: 578px; text-align: center;
    font-family: "Anton", sans-serif; font-size: 96px; line-height: 102px;
    color: var(--teal); white-space: nowrap;
  }
  .front-subtitle {
    position: absolute; left: 661px; top: 318px; width: 500px; text-align: center;
    font-family: "Pathway Gothic One", sans-serif; font-size: 22px; line-height: 26px; color: var(--ink);
  }
  .fog-art {
    position: absolute; left: 622px; top: 384px; width: 578px; height: 513px;
    background:
      radial-gradient(ellipse 70% 22% at 30% 35%, rgba(255,255,255,0.9) 0%, rgba(255,255,255,0) 100%),
      radial-gradient(ellipse 60% 20% at 75% 60%, rgba(255,255,255,0.85) 0%, rgba(255,255,255,0) 100%),
      radial-gradient(ellipse 80% 25% at 45% 85%, rgba(255,255,255,0.7) 0%, rgba(255,255,255,0) 100%),
      linear-gradient(to bottom, var(--white) 0%, var(--mist) 35%, var(--teal-soft) 75%, var(--teal) 100%);
  }
</style>
</head>
<body>
<div class="cover">
  <section class="back-panel">
    <h2 class="back-title">WALKING OUT OF THE FOG</h2>
    <p class="back-blurb">Millions of people feel the pain, loneliness, and agony of anxiety and depression every day. Many turn to Western medicine in the hopes that a pill will ease the pain and make the problem go away. Oftentimes, this only makes matters worse and doesn’t address the root cause. No one should have to struggle like this when natural answers exist that can address the physical, energetic, emotional, or spiritual causes of anxiety and depression. For 11 long years, Dr. Vance personally struggled with heavy depression until he discovered answers that helped him to completely heal. Walking Out of the Fog is a guide that will help you discover - The two root physical causes of depression and exactly what to do to start healing today - How the negative emotions we have stored within from trauma and bad experiences can drive depression - Tools from Chinese medicine, applied kinesiology, and tapping to help you free your mind and live in peace - An actionable plan to help you let go of the pain, suffering, and negative emotions from your past. Whether you feel depressed and anxious or know someone who struggles with these issues, Walking Out of the Fog will transform how you think about depression and will give you the tools to heal so that you can be free and live in peace.</p>
    <p class="author-bio"><strong>DR. VANCE HOLBROOK</strong> is a board-certified acupuncture physician licensed in the state of Florida. He received his training at the Calder Institute of Holistic Practice. He also graduated with a master’s degree in counseling and psychology from Meadowbrook Seminary of Theology. His mission is to help people transform their health and improve the quality of their life naturally. He lives in Orlando, FL where he runs a holistic medical clinic called Bluepine Wellness Center.</p>
    <ul class="contact-list">
      <li>www.drvanceholbrook-example.com</li>
      <li>Instagram: drvanceholbrook</li>
      <li>Facebook: bluepinewellnesscenter</li>
    </ul>
    <div class="author-photo" role="img" aria-label="Small portrait photograph of the author"></div>
    <div class="brand-name"><span class="brand-square"></span><span>Dr. Vance<br>Holbrook</span></div>
    <div class="spine-title">WALKING OUT OF THE FOG</div>
    <div class="spine-author">Dr. Vance Holbrook</div>
  </section>

  <section class="front">
    <h1 class="front-author">Dr. Vance Holbrook, AP, MA</h1>
    <div class="front-title">WALKING OUT<br>OF THE FOG</div>
    <p class="front-subtitle">How to use tapping, applied kinesiology, and Chinese medicine to heal your body, free your mind and live in peace</p>
    <div class="fog-art" role="img" aria-label="Soft drifting fog lifting into clear teal light"></div>
  </section>
</div>
</body>
</html>
```